Consultancy company needs flyer design

We need a flyer design for a new service to be provided. It is a service in which project management is outsourced. Text of the service has been attached (in Dutch).
We would like the design to be in line with our website design (www.veltoris.com). Also we would like to re-use the main banner of the site (see attachment)

Industry/Entity Type

It Company

Requirements
Must have
• Flyer must be double sided

```html
<!DOCTYPE html>
<html lang="nl">
<head>
<meta charset="utf-8">
<title>Veltoris – PMAAS flyer</title>
<link href="https://fonts.googleapis.com/css2?family=Source+Sans+3:wght@400;600;700&display=swap" rel="stylesheet">
<style>
:root{
  --brown:#7d6a45;
  --gold:#8c7646;
  --dark:#3b3a3d;
  --band:#e9e9ea;
  --text:#3a3a3a;
  --white:#ffffff;
  --stage:#dcd9d5;
}
*{margin:0;padding:0;box-sizing:border-box}
html,body{width:1200px;height:841px;overflow:hidden}
body{background:var(--stage);font-family:"Source Sans 3",Arial,sans-serif;color:var(--text);position:relative}
.flyer{position:absolute;top:61px;width:508px;height:720px;background:var(--white);overflow:hidden}
.flyer--front{left:61px}
.flyer--back{left:623px}
.abs{position:absolute}

/* front */
.hero-gears{left:0;top:0;width:508px;height:162px;background:linear-gradient(120deg,#1f2a38 0%,#5c6b7c 40%,#aab4be 60%,#3b4656 100%)}
.brand{display:flex;align-items:center;gap:8px}
.brand-dot{width:10px;height:10px;border-radius:50%;background:var(--gold)}
.brand--front{left:24px;top:62px}
.brand--front .brand-name{color:var(--white);font-size:28px;font-weight:600;line-height:1}
.title-band{left:0;top:162px;width:508px;height:68px;background:var(--band);display:flex;align-items:center;justify-content:center;text-align:center}
.title-band h1{color:var(--gold);font-size:13.5px;font-weight:600;line-height:1.55;text-transform:uppercase;width:440px}
.intro{left:16px;top:236px;width:236px;font-size:9.6px;line-height:1.35;text-align:justify}
.issues{left:16px;top:295px;width:244px;list-style:none;font-size:9.6px;line-height:1.3}
.issues li{position:relative;padding-left:18px;margin-bottom:8px}
.issues li::before{content:"";position:absolute;left:0;top:1px;width:10px;height:10px;border-radius:50%;background:var(--brown)}
.alt{left:16px;top:452px;width:236px;font-size:9.6px;line-height:1.35;text-align:justify}
.alt p{margin-bottom:11px}
.side-panel{left:277px;top:229px;width:231px;height:431px;background:var(--brown);color:var(--white)}
.tab{position:absolute;left:3px;width:178px;height:20px;background:var(--white);color:#222;font-size:10px;font-weight:600;padding:3px 11px;text-transform:uppercase}
.side-list{position:absolute;left:13px;width:212px;list-style:none;font-size:8px;line-height:1.1}
.side-list li{position:relative;padding-left:10px;margin-bottom:4px}
.side-list li::before{content:"";position:absolute;left:0;top:2px;width:5px;height:5px;border-radius:50%;border:1px solid var(--white)}
.side-note{position:absolute;left:13px;width:210px;font-size:8.2px;line-height:1.2}
.side-note em{font-weight:700}
.photo-round{border-radius:50%;border:3px solid var(--white);box-shadow:0 2px 4px rgba(0,0,0,.25)}
.photo-sepia{background:radial-gradient(circle at 40% 40%,#e9dccb,#a88a66 70%,#6e5638)}
.footer{left:0;top:660px;width:508px;height:60px;background:var(--dark);display:flex;align-items:center}
.footer--front{justify-content:flex-end;padding-right:16px;gap:10px}
.footer--front .lead{color:var(--gold);font-size:12px}
.footer--front .url{color:var(--white);font-size:16px}

/* back */
.hero-handshake{left:0;top:0;width:508px;height:223px;background:linear-gradient(100deg,#e8e8e8 0%,#b9bcbf 35%,#a07a5e 50%,#c4c6c8 65%,#6c7075 100%)}
.claim-band{left:0;top:223px;width:508px;height:57px;background:var(--brown);display:flex;align-items:center;justify-content:center}
.claim-band h2{color:var(--white);font-size:13px;font-weight:600;text-align:center;line-height:1.55;text-transform:uppercase;width:420px}
.brand--back{left:22px;top:296px}
.brand--back .brand-dot{width:12px;height:12px}
.brand--back .brand-name{color:#2e2e2e;font-size:34px;font-weight:600;line-height:1}
.about-head{left:25px;top:370px;font-size:11.5px;font-weight:600;color:#222;text-transform:uppercase}
.about-head span{color:var(--gold)}
.about{left:25px;top:390px;width:465px;font-size:10.6px;line-height:1.3}
.about p{margin-bottom:12px}
.ring{width:122px;height:122px;border-radius:50%;border:3px solid var(--gold);border-right-color:#e6dccb;border-bottom-color:#d9c9ae;padding:5px}
.ring .photo-sepia{width:100%;height:100%;border-radius:50%}
.shadow{width:100px;height:8px;border-radius:50%;background:radial-gradient(rgba(0,0,0,.25),transparent 70%)}
.footer--back{justify-content:space-between;padding:0 20px 0 24px;color:var(--white);font-size:13px}
.contact{display:flex;align-items:center;gap:6px}
.contact svg{fill:var(--gold)}
</style>
</head>
<body>

<section class="flyer flyer--front">
  <div class="abs hero-gears" role="img" aria-label="Close-up of metal gears and machinery"></div>
  <div class="abs brand brand--front"><span class="brand-dot"></span><span class="brand-name">Veltoris</span></div>
  <div class="abs title-band"><h1>Ontzorging van uw projectdelivery: project management as a service (PMAAS)</h1></div>

  <p class="abs intro">U kunt voor de realisatie van uw projectportfolio de hulp inroepen van externe projectmanagers, en daarbij zelf de coördinatie verzorgen. Grote kans dat u dan tegen één of meer van de volgende zaken aanloopt:</p>
  <ul class="abs issues">
    <li>Een wisselende kwaliteit van project managers</li>
    <li>Problemen om kosten inzichtelijk en voorspelbaar of beheersbaar houden (management rapportage)</li>
    <li>Een ad hoc relatie met uw project managers en leveranciers</li>
    <li>Beperkt leergedrag en herhaling van fouten</li>
    <li>Tijdverlies en kosten omdat u veel tijd kwijt bent aan uitleg van rand voorwaardelijke zaken</li>
  </ul>
  <div class="abs alt">
    <p>Een alternatief is onze PMAAS-service. Die bevat alle ingrediënten om uw projectenportfolio kostenefficiënt en op hoog kwaliteitsniveau te realiseren. Veltoris zorgt voor inzet van projectmanagers die al 'up to speed' zijn als ze bij u binnenkomen.</p>
    <p>Ze hebben de juiste expertise, zijn al ingewerkt op uw of onze standaard methodiek en op uw organisatorische setting. En heeft u ineens meer of minder werk? Geen probleem. Dan schalen wij net zo gemakkelijk op en af.</p>
  </div>

  <div class="abs side-panel">
    <div class="tab" style="top:10px">Wij zorgen voor</div>
    <ul class="side-list" style="top:37px">
      <li>Een eenduidige werkwijze, rapportering en gebruik van tooling</li>
      <li>Een scherpe intake en voorbereidingsfase van de te starten projecten</li>
      <li>De benodigde op-en afschaling van project managers met het juiste profiel</li>
      <li>Ingewerkte projectmanagers op de overeen gekomen project methode</li>
      <li>Continue monitoring op afgesproken kpi's over de projecten heen</li>
      <li>Periodiek overleg over de performance</li>
      <li>Continue verbetering op basis van klantevaluaties</li>
      <li>Facturatie volgens afspraak (milestone-based)</li>
    </ul>
    <div class="tab" style="top:196px">U zorgt voor</div>
    <ul class="side-list" style="top:223px">
      <li>Een up to date forecast van de te realiseren project portfolio</li>
      <li>Een goede projectbrief als basis voor onze intake</li>
    </ul>
    <p class="side-note" style="top:270px"><em>Kortom: laat u ontzorgen in uw project delivery!</em></p>
    <div class="tab" style="top:295px">PMO en PPM</div>
    <p class="side-note" style="top:324px;text-align:justify">Wilt u zich nog meer laten ontzorgen? Dat kan! Naast onze PMAAS-service leveren wij ook diensten op het gebied van Project Management Office (PMO) en/of Project Portfolio Management (PPM).</p>
    <p class="side-note" style="top:384px;text-align:justify">Wij kunnen deze activiteiten voor u opzetten, maar ook de operationele aansturing ervan ondersteunen of voor onze rekening nemen.</p>
  </div>

  <div class="abs photo-round photo-sepia" style="left:7px;top:591px;width:88px;height:88px" role="img" aria-label="Sepia photo of harbour cranes"></div>
  <div class="abs photo-round photo-sepia" style="left:101px;top:591px;width:88px;height:88px" role="img" aria-label="Sepia photo of a tugboat"></div>
  <div class="abs photo-round photo-sepia" style="left:195px;top:591px;width:88px;height:88px" role="img" aria-label="Sepia photo of industrial installation"></div>

  <div class="abs footer footer--front"><span class="lead">Wilt u meer weten, bekijk onze website:</span><span class="url">www.veltoris.com</span></div>
</section>

<section class="flyer flyer--back">
  <div class="abs hero-handshake" role="img" aria-label="Business handshake in front of a world map"></div>
  <div class="abs claim-band"><h2>Realisatie van veranderingsprocessen door toepassing van innovatieve methoden</h2></div>
  <div class="abs brand brand--back"><span class="brand-dot"></span><span class="brand-name">Veltoris</span></div>

  <h3 class="abs about-head"><span>Veltoris:</span> Innovatief in verandertrajecten</h3>
  <div class="abs about">
    <p>Als management consultancy bureau houden wij ons bezig met de begeleiding van veranderingen in bedrijven. Op het gebied van strategie, maar ook van processen en systemen. Wij onderscheiden ons door toepassing van visualisatie technieken, bedrijfsproces simulaties en unieke services en zijn continu op zoek naar nieuwe toepassingsmogelijkheden op dit gebied.</p>
    <p>Door de krachten van uw medewerkers en die van ons te verenigen, komen we tot betere en snellere resultaten. Daarbij gaan wij samen op reis. Want veranderingen kun je niet leren, je moet ze ervaren.</p>
  </div>

  <div class="abs ring" style="left:30px;top:515px"><div class="photo-sepia" role="img" aria-label="Sepia photo of a cargo ship"></div></div>
  <div class="abs shadow" style="left:41px;top:642px"></div>
  <div class="abs ring" style="left:193px;top:515px"><div class="photo-sepia" role="img" aria-label="Sepia photo of a truck front"></div></div>
  <div class="abs shadow" style="left:204px;top:642px"></div>
  <div class="abs ring" style="left:353px;top:515px"><div class="photo-sepia" role="img" aria-label="Sepia photo of a ship hull at a quay"></div></div>
  <div class="abs shadow" style="left:364px;top:642px"></div>

  <div class="abs footer footer--back">
    <span class="contact"><svg width="10" height="14" viewBox="0 0 10 14"><path d="M5 0a5 5 0 0 0-5 5c0 4 5 9 5 9s5-5 5-9a5 5 0 0 0-5-5zm0 7a2 2 0 1 1 0-4 2 2 0 0 1 0 4z"/></svg>Lindelaan 12 - 3712 KM Zeist</span>
    <span class="contact"><svg width="12" height="12" viewBox="0 0 12 12"><path d="M2.5 0 4.5 2.6 3.4 4a7 7 0 0 0 4.6 4.6L9.4 7.5 12 9.5 10.6 12C5 12 0 7 0 1.4z"/></svg>085 - 0417728</span>
    <span class="contact"><svg width="13" height="9" viewBox="0 0 13 9"><rect width="13" height="9"/></svg>info@veltoris.com</span>
  </div>
</section>

</body>
</html>
```